Website Comps for Famous Southern BBQ Restaurant in Alabama

We need an authentic, brand-focused redesign for a restaurant.

We need an authentic look.
The client really likes this website.
https://pelzerpit.com/

I don't want to see a bunch of crazy colors.
Avoid image sliders on the homepage. I hate those.

Please mockup the following three pages:
Homepage
Interior page (for mockup purposes, you can do an About page)
Menu page

I only need the PSD's; not the website coded.

Here is the current website: www.dunmoresmokehouse.com

https://pelzerpit.com/

Here are some additional stock photos. New photos will be shot, but these may help for your mock-up designs.
https://www.filecrate.net/sh/83kqvtrpe21zwa9/QXM71bTr4-plWnfVoe8KtYjd?dl=0
Updates

I realize we don't have a lot of high-quality photos to work with.Those will be shot.Here are some additional stock photos that may help.https://www.filecrate.net/sh/83kqvtrpe21zwa9/QXM71bTr4-plWnfVoe8KtYjd?dl=0 Added Saturday, June 10, 2017

Target Market(s)

United states

Industry/Entity Type

Restaurant

Number of Pages Required

3 page

Font styles to use
Sans Serif

Colors

Designer to choose colors to be used in the design.

Requirements
Must have
• An authentic look.
• The client really likes this website.
• https://pelzerpit.com/
• It's simple, bold, and vintage at the same time.
• That is what we want.
• Our existing website is
• dunmoresmokehouse.com
Nice to have
• Simplicity. Something that makes the food look good.
• Possibly a background.
• Logo:
• https://www.filecrate.net/s/k58tnwpl3ovza2e/dunmore-smokehouse-ridgeway.png?dl=0
• Here is a sampling of photos for your comps:
• https://www.filecrate.net/sh/61vbqzhoewpxtn4/QLT4b8JKyRmPPwf6c2ZnHUVpe?dl=0
Should not have
• Nothing too busy.
• Not too many colors.
• Keep it simple, authentic, "down home."
• No homepage image sliders.

```html
<!DOCTYPE html>
<html lang="en">
<head>
<meta charset="utf-8">
<title>Dunmore Smokehouse</title>
<link rel="stylesheet" href="https://fonts.googleapis.com/css2?family=Roboto:wght@400;500&family=Roboto+Condensed:wght@400;700&family=Lobster&display=swap">
<style>
  :root {
    --red: #ee3a46;
    --orange: #f6a41f;
    --brown: #3a1a12;
    --ink: #1e1e1e;
    --text: #4a4a4a;
    --muted: #8a8a8a;
    --page: #f4f4f4;
    --white: #ffffff;
  }
  * { margin: 0; padding: 0; box-sizing: border-box; }
  html, body { width: 718px; height: 1200px; overflow: hidden; background: var(--page); }
  body { position: relative; font-family: "Roboto", sans-serif; color: var(--text); }

  .site-header { position: absolute; top: 0; left: 0; width: 718px; height: 37px; background: var(--white); z-index: 3; box-shadow: 0 1px 2px rgba(0,0,0,.08); }
  .brand-tab { position: absolute; left: 113px; top: 0; width: 94px; height: 74px; background: var(--white); box-shadow: 0 2px 4px rgba(0,0,0,.2); display: flex; align-items: center; justify-content: center; }
  .brand-tab .brand-name { font-family: "Roboto Condensed", sans-serif; font-weight: 700; font-size: 13px; line-height: 1.05; color: var(--red); text-align: center; text-transform: uppercase; }
  .main-nav { position: absolute; left: 253px; top: 0; display: flex; height: 37px; }
  .main-nav a { position: relative; display: block; padding: 0 5.3px; line-height: 37px; font-size: 7px; letter-spacing: .1px; color: var(--text); text-decoration: none; text-transform: uppercase; }
  .main-nav a.is-active::after { content: ""; position: absolute; left: 0; right: 0; bottom: -2px; height: 3px; background: var(--red); }

  .hero { position: absolute; top: 37px; left: 0; width: 718px; height: 335px;
    background:
      radial-gradient(ellipse 260px 120px at 560px 170px, rgba(176,110,58,.55), rgba(176,110,58,0) 70%),
      radial-gradient(ellipse 220px 110px at 110px 150px, rgba(150,120,95,.5), rgba(150,120,95,0) 70%),
      radial-gradient(ellipse 420px 90px at 400px 40px, rgba(120,120,135,.45), rgba(120,120,135,0) 70%),
      linear-gradient(180deg, #4e4037 0%, #3a2e27 45%, #2a221d 75%, #1e1915 100%); }
  .hero h1 { position: absolute; top: 140px; left: 0; width: 718px; font-family: "Roboto Condensed", sans-serif; font-weight: 700; font-size: 23px; line-height: 27px; color: var(--white); text-align: center; text-transform: uppercase; letter-spacing: -.3px; text-shadow: 0 1px 3px rgba(0,0,0,.6); }

  .locations { position: absolute; top: 393px; left: 112px; width: 494px; height: 177px; display: flex; }
  .location-list { width: 281px; }
  .location-list a { display: flex; align-items: center; padding-left: 13px; font-family: "Roboto Condensed", sans-serif; font-weight: 400; font-size: 15.5px; color: var(--white); text-decoration: none; text-transform: uppercase; }
  .location-list .is-red { background: var(--red); }
  .location-list .is-orange { background: var(--orange); }
  .location-photo { flex: 1;
    background:
      radial-gradient(circle 22px at 150px 112px, rgba(214,52,52,.85), rgba(214,52,52,0) 100%),
      radial-gradient(ellipse 40px 60px at 80px 140px, rgba(38,40,70,.9), rgba(38,40,70,0) 100%),
      radial-gradient(ellipse 60px 40px at 150px 40px, rgba(220,215,205,.5), rgba(220,215,205,0) 100%),
      linear-gradient(160deg, #9a9d98 0%, #7b7f7b 45%, #5d605d 70%, #2f2e36 100%); }

  .info { position: absolute; top: 602px; left: 0; width: 718px; }
  .info-col { position: absolute; top: 0; width: 260px; text-align: center; }
  .info-col.hours { left: 109px; }
  .info-col.place { left: 367px; }
  .info-col .icon { height: 50px; display: flex; align-items: center; justify-content: center; }
  .info-col h2 { margin-top: 14px; font-weight: 400; font-size: 16px; line-height: 18px; color: var(--ink); }
  .info-col p { font-size: 12px; line-height: 15px; color: var(--text); }
  .hours p { margin-top: 7px; line-height: 20px; }
  .place p { margin-top: 9px; }
  .place p + p { margin-top: 9px; }

  .store { position: absolute; top: 792px; left: 0; width: 718px; height: 263px; text-align: center;
    background:
      radial-gradient(ellipse 160px 120px at 120px 120px, rgba(222,140,20,.45), rgba(222,140,20,0) 70%),
      radial-gradient(ellipse 180px 110px at 600px 90px, rgba(250,190,90,.45), rgba(250,190,90,0) 70%),
      linear-gradient(180deg, #f3a429 0%, #f1a125 100%); }
  .store h2 { margin-top: 44px; font-family: "Lobster", cursive; font-weight: 400; font-size: 47px; line-height: 56px; color: var(--white); }
  .store .shop-button { display: inline-block; margin-top: 22px; width: 129px; height: 27px; line-height: 25px; border: 1.5px solid var(--white); border-radius: 4px; font-size: 9px; font-weight: 500; color: var(--white); text-decoration: none; text-transform: uppercase; }

  .site-footer { position: absolute; top: 1055px; left: 0; width: 718px; height: 145px; background: var(--white); text-align: center; }
  .footer-brand { display: inline-flex; align-items: center; justify-content: center; margin-top: 26px; width: 48px; height: 48px; background: var(--brown); font-family: "Roboto Condensed", sans-serif; font-weight: 700; font-size: 8px; line-height: 1.1; color: var(--orange); text-transform: uppercase; }
  .social { display: flex; justify-content: center; gap: 7px; margin-top: 17px; }
  .social a { width: 13px; height: 13px; border: 1px solid var(--ink); border-radius: 50%; display: flex; align-items: center; justify-content: center; }
  .social a::after { content: ""; width: 4px; height: 4px; border-radius: 50%; background: var(--ink); }
  .copyright { margin-top: 6px; font-size: 7px; color: var(--muted); }
  .footer-band { position: absolute; left: 0; bottom: 0; width: 718px; height: 20px; }
</style>
</head>
<body>
  <header class="site-header">
    <div class="brand-tab">
      <span class="brand-name">Dunmore<br>Smokehouse</span>
    </div>
    <nav class="main-nav">
      <a href="#" class="is-active">Home</a>
      <a href="#">About</a>
      <a href="#">Locations</a>
      <a href="#">Restaurant Menus</a>
      <a href="#">Catering</a>
      <a href="#">News</a>
      <a href="#">Store</a>
      <a href="#">Contact Us</a>
    </nav>
  </header>

  <section class="hero" role="img" aria-label="Photo of the restaurant bar with diners, flags and vintage signs on the walls">
    <h1>Ridgeway, AL named as one of<br>Harbor Ledger’s 52 places<br>to visit in 2017</h1>
  </section>

  <section class="locations">
    <div class="location-list">
      <a href="#" class="is-red" style="height:64px">Dunmore Smokehouse - Elm Hollow</a>
      <a href="#" class="is-orange" style="height:49px">Dunmore Soul Kitchen - Briar Park</a>
      <a href="#" class="is-red" style="height:64px">Dunmore Juke Joint - Foxridge</a>
    </div>
    <div class="location-photo" role="img" aria-label="Photo of a restaurant wall with a hanging t-shirt and vintage signs"></div>
  </section>

  <section class="info">
    <div class="info-col hours">
      <div class="icon">
        <svg width="46" height="46" viewBox="0 0 46 46" aria-hidden="true">
          <circle cx="23" cy="23" r="20.5" fill="none" stroke="var(--red)" stroke-width="4"/>
          <path d="M23 11 V24 H33" fill="none" stroke="var(--red)" stroke-width="4" stroke-linecap="round"/>
        </svg>
      </div>
      <h2>HOURS</h2>
      <p>Mon - Sat: 11:00 am - 8 pm<br>Mon - Sat: 11:00 am - 8 pm Sun: 11:00 am - 4 pm<br>Mon - Sat: 11:00 am - 12:00 am/midnight</p>
    </div>
    <div class="info-col place">
      <div class="icon">
        <svg width="36" height="48" viewBox="0 0 36 48" aria-hidden="true">
          <path d="M18 47 C12 38 1 27 1 17 A17 17 0 0 1 35 17 C35 27 24 38 18 47 Z" fill="var(--red)"/>
          <circle cx="18" cy="17" r="6.5" fill="var(--page)"/>
        </svg>
      </div>
      <h2>LOCATION</h2>
      <p>1412 Millbrook Road Ridgeway AL 35990<br>Phone: (205) 555-0142</p>
      <p>308 Cedar Ave South Ridgeway, AL 35991<br>(205) 555-0187</p>
    </div>
  </section>

  <section class="store" role="img" aria-label="Orange-tinted photo of the restaurant dining room">
    <h2>Welcome to<br>Dunmore’s online store!</h2>
    <a href="#" class="shop-button">Shop Now</a>
  </section>

  <footer class="site-footer">
    <div class="footer-brand">Dunmore<br>Smoke<br>house</div>
    <div class="social">
      <a href="#" aria-label="Social link 1"></a>
      <a href="#" aria-label="Social link 2"></a>
      <a href="#" aria-label="Social link 3"></a>
      <a href="#" aria-label="Social link 4"></a>
    </div>
    <p class="copyright">Copyright 2017 Dunmore Smokehouse, LLC</p>
    <svg class="footer-band" viewBox="0 0 718 20" aria-hidden="true">
      <path d="M0 14 H336 L359 0 L382 14 H718 V20 H0 Z" fill="var(--red)"/>
    </svg>
  </footer>
</body>
</html>
```